Logo for hot realtor starting a team
The Lusk Team
Professional
Vernon Lusk III
See Attached photo
vernonlusk03@postlark.net
www.allbrackenvalehomesforsale.com
Slogan to be used - "Every Deal Closed By A Lusk"
Personal Picture and contact number
Reference draft #10 - I really like this one for a business card and I am looking for a new business card design and have a contest for this one. I will make sure to send you a request for a design. These are the changes that I would like to see and if you can make this happen, this is the winning business card, see below:
Change the style from cursive to manual script. Make the picture of what appears to be a Rose look more like a Rose. also make the font larger.
Remove the address completely and replace with my website (www.allbrackenvalehomesforsale.com and add contact number: 555-214-0386.
I would like the card to also be gray in color with black writing

```html
<!DOCTYPE html>
<html lang="en">
<head>
<meta charset="utf-8">
<title>The Lusk Team – Business Card</title>
<link href="https://fonts.googleapis.com/css2?family=Cinzel:wght@600;700&family=Montserrat:wght@400;500&display=swap" rel="stylesheet">
<style>
  :root {
    --canvas: #e9e9ea;
    --card-black: #0d0d0e;
    --card-edge: #1c1c1e;
    --rose-red: #c8222a;
    --deep-red: #6e1116;
    --ink-white: #f2f2f2;
    --soft-gray: #9a9a9d;
    --faint-red: #3a0d10;
  }
  * { margin: 0; padding: 0; box-sizing: border-box; }
  html, body {
    width: 1200px; height: 980px; overflow: hidden;
    background: var(--canvas);
  }
  .sheet {
    width: 1200px; height: 980px;
    display: flex; flex-direction: column; align-items: center; justify-content: center;
    gap: 60px;
  }
  .card {
    position: relative;
    width: 700px; height: 400px;
    border-radius: 22px;
    background: var(--card-black);
    overflow: hidden;
    box-shadow: 0 10px 30px rgba(0,0,0,0.25);
  }

  /* Front */
  .brand {
    position: absolute; left: 58px; top: 46px;
    display: flex; align-items: center; gap: 14px;
  }
  .brand-mark {
    width: 18px; height: 18px; background: var(--rose-red);
  }
  .brand-name {
    font-family: 'Cinzel', serif; font-weight: 700;
    font-size: 40px; letter-spacing: 1px;
    color: var(--ink-white); text-transform: uppercase;
  }
  .slogan {
    position: absolute; left: 90px; top: 102px;
    font-family: 'Montserrat', sans-serif; font-weight: 400;
    font-size: 15px; letter-spacing: 1px; color: var(--rose-red);
  }
  .agent-name {
    position: absolute; left: 58px; top: 160px;
    font-family: 'Montserrat', sans-serif; font-weight: 500;
    font-size: 19px; letter-spacing: 3px; font-variant: small-caps;
    color: var(--ink-white);
  }
  .contact-list {
    position: absolute; left: 58px; top: 222px;
    list-style: none;
    font-family: 'Montserrat', sans-serif; font-size: 14px;
    color: var(--ink-white); letter-spacing: 0.8px;
  }
  .contact-list li {
    display: flex; align-items: center; gap: 12px;
    height: 30px;
  }
  .contact-icon { width: 18px; height: 18px; flex: none; }
  .swoosh { position: absolute; right: 0; bottom: 0; }

  /* Back */
  .back-web {
    position: absolute; left: 40px; top: 34px;
    font-family: 'Montserrat', sans-serif; font-size: 14px;
    letter-spacing: 2px; color: var(--soft-gray); text-transform: uppercase;
  }
  .back-brand {
    position: absolute; left: 0; right: 0; top: 150px;
    text-align: center;
    font-family: 'Cinzel', serif; font-weight: 700;
    font-size: 78px; letter-spacing: 2px; text-transform: uppercase;
    color: var(--faint-red);
  }
</style>
</head>
<body>
<main class="sheet">

  <section class="card card-front" aria-label="Business card front">
    <div class="brand">
      <span class="brand-mark"></span>
      <span class="brand-name">The Lusk Team</span>
    </div>
    <p class="slogan">Every Deal Closed By A Lusk</p>
    <h1 class="agent-name">Vernon Lusk III</h1>

    <ul class="contact-list">
      <li>
        <svg class="contact-icon" viewBox="0 0 18 18"><circle cx="9" cy="9" r="9" fill="#f2f2f2"/><path d="M6 4.5 L7.6 4.5 L8.3 6.8 L7.2 7.6 Q8 9.8 10.4 10.8 L11.2 9.7 L13.5 10.4 L13.5 12 Q13 13.5 11.5 13.4 Q5.2 12.5 4.6 6 Q4.6 4.8 6 4.5 Z" fill="#0d0d0e"/></svg>
        555-308-1947
      </li>
      <li>
        <svg class="contact-icon" viewBox="0 0 18 18"><circle cx="9" cy="9" r="9" fill="#f2f2f2"/><rect x="6" y="3.5" width="6" height="11" rx="1.2" fill="#0d0d0e"/><rect x="7" y="5" width="4" height="7" fill="#f2f2f2"/></svg>
        555-214-0386
      </li>
      <li>
        <svg class="contact-icon" viewBox="0 0 18 18"><circle cx="9" cy="9" r="9" fill="#f2f2f2"/><rect x="4.5" y="5.5" width="9" height="7" fill="#0d0d0e"/><path d="M4.8 5.8 L9 9.5 L13.2 5.8" stroke="#f2f2f2" stroke-width="1" fill="none"/></svg>
        vernonlusk03@postlark.net
      </li>
      <li>
        <svg class="contact-icon" viewBox="0 0 18 18"><circle cx="9" cy="9" r="9" fill="#f2f2f2"/><circle cx="9" cy="9" r="5" fill="none" stroke="#0d0d0e" stroke-width="1.2"/><path d="M4 9 H14 M9 4 Q6 9 9 14 M9 4 Q12 9 9 14" stroke="#0d0d0e" stroke-width="1" fill="none"/></svg>
        www.allbrackenvalehomesforsale.com
      </li>
    </ul>

    <svg class="swoosh" width="420" height="400" viewBox="0 0 420 400" aria-hidden="true">
      <path d="M420 40 Q250 120 150 400 L420 400 Z" fill="var(--rose-red)"/>
      <path d="M420 75 Q290 150 205 400 L420 400 Z" fill="var(--card-black)"/>
      <path d="M420 110 Q320 180 260 400" stroke="var(--soft-gray)" stroke-width="3" fill="none"/>
      <path d="M420 20 Q230 110 120 400" stroke="var(--deep-red)" stroke-width="2" fill="none"/>
    </svg>
  </section>

  <section class="card card-back" aria-label="Business card back">
    <p class="back-web">www.allbrackenvalehomesforsale.com</p>
    <p class="back-brand">The Lusk Team</p>
  </section>

</main>
</body>
</html>
```